Brightpath Wellness Partners

Please design a business card that is colorful but at the same time easy to read. We are based out on Miami Florida. We are a small start up healthcare company that has been in operation for 1 year. Our clients are Hospitals, Insurance companies, and Manage Care health companies. We are growing quickly and lead the niche we are in. Please make the card 2 sided on the front will be the typical info. Logo, Company Name, Persons Name, Title, Cell #, Office #, Fax#, email, website. No address. On the back we will list 5 services that we do. For example Care Transitions, Case management, Risk assessment, Utilization Review.
Target Market(s)
CEO's and COO's of hospitals and healthcare companies.
Industry/Entity Type
Healthcare

```html
<!DOCTYPE html>
<html lang="en">
<head>
<meta charset="utf-8">
<title>Brightpath Wellness Partners – Business Card</title>
<link href="https://fonts.googleapis.com/css2?family=Lato:ital,wght@0,400;0,700;0,900;1,700&display=swap" rel="stylesheet">
<style>
  :root {
    --stage: #4a4a4a;
    --card-white: #ffffff;
    --ink: #1c1c1c;
    --label-blue: #1f4fa8;
    --name-green: #1fa34a;
    --mark-blue: #2b3f9e;
    --mark-sky: #2aa3e0;
    --back-top: #2e2e2e;
    --back-bottom: #1b1b1b;
    --band: #141414;
    --brand-grey: #8a8a8a;
    --service-blue: #2f55c8;
  }
  * { margin: 0; padding: 0; box-sizing: border-box; }
  html, body {
    width: 1200px;
    height: 926px;
    overflow: hidden;
    background: var(--stage);
    font-family: "Lato", Arial, sans-serif;
  }
  .canvas {
    position: relative;
    width: 1200px;
    height: 926px;
  }
  .card {
    position: absolute;
    width: 600px;
    height: 343px;
    border-radius: 4px;
    overflow: hidden;
    box-shadow: 0 10px 28px rgba(0,0,0,0.35);
  }

  /* Front */
  .card-front {
    left: 80px;
    top: 480px;
    background: var(--card-white);
  }
  .front-company {
    position: absolute;
    left: 36px;
    top: 40px;
    font-size: 27px;
    font-weight: 400;
    color: var(--ink);
  }
  .front-person {
    position: absolute;
    left: 36px;
    top: 112px;
    font-size: 25px;
    color: var(--name-green);
    font-weight: 400;
  }
  .front-person strong { font-weight: 700; }
  .front-person .title {
    font-size: 14px;
    font-weight: 900;
    color: var(--ink);
    letter-spacing: 0.5px;
  }
  .contact-list {
    position: absolute;
    left: 36px;
    top: 156px;
    list-style: none;
    font-size: 15px;
    line-height: 22px;
    color: var(--ink);
  }
  .contact-list .label {
    color: var(--label-blue);
    font-weight: 700;
    font-style: italic;
  }
  .front-accent {
    position: absolute;
    right: -70px;
    top: 90px;
  }

  /* Back */
  .card-back {
    left: 520px;
    top: 110px;
    background: linear-gradient(180deg, var(--back-top), var(--back-bottom));
  }
  .back-brand {
    position: absolute;
    left: 0;
    right: 0;
    top: 70px;
    display: flex;
    align-items: center;
    justify-content: center;
    gap: 18px;
  }
  .back-brand-name {
    font-size: 30px;
    font-weight: 900;
    line-height: 1.1;
    color: var(--brand-grey);
  }
  .service-band {
    position: absolute;
    left: 0;
    right: 0;
    top: 196px;
    height: 96px;
    background: var(--band);
    display: flex;
    align-items: center;
    justify-content: center;
    text-align: center;
  }
  .service-list {
    font-size: 14px;
    letter-spacing: 1.2px;
    line-height: 20px;
    color: var(--service-blue);
    text-transform: uppercase;
  }
</style>
</head>
<body>
  <main class="canvas">

    <section class="card card-back" aria-label="Business card back">
      <div class="back-brand">
        <svg width="64" height="64" viewBox="0 0 64 64" aria-hidden="true">
          <circle cx="32" cy="32" r="30" fill="var(--mark-blue)"/>
        </svg>
        <div class="back-brand-name">Brightpath<br>Wellness Partners</div>
      </div>
      <div class="service-band">
        <p class="service-list">Care transitions, case management,<br>risk assessment, utilization review and manage care</p>
      </div>
    </section>

    <section class="card card-front" aria-label="Business card front">
      <h1 class="front-company">Brightpath Wellness Partners</h1>
      <p class="front-person">Daniel <strong>Reyes</strong> <span class="title">-TITLE</span></p>
      <ul class="contact-list">
        <li><span class="label">cell:</span> 123-456-7890</li>
        <li><span class="label">office:</span> 098-765-4321</li>
        <li><span class="label">fax:</span> 123-098-4567</li>
        <li><span class="label">email:</span> yourdomain.com</li>
        <li><span class="label">web:</span> yourname@yourdomain.com</li>
      </ul>
      <svg class="front-accent" width="300" height="300" viewBox="0 0 300 300" aria-hidden="true">
        <defs>
          <linearGradient id="accentFill" x1="0" y1="0" x2="0" y2="1">
            <stop offset="0" stop-color="var(--mark-blue)"/>
            <stop offset="1" stop-color="var(--mark-sky)"/>
          </linearGradient>
        </defs>
        <circle cx="150" cy="150" r="140" fill="url(#accentFill)"/>
      </svg>
    </section>

  </main>
</body>
</html>
```